Brightwire Hollow Business cards

one side I would like my logo (uploaded) and the other side I want my details. I'm an electrician in sydney. The logo side I'm happy with just a white background and our logo in the middle.

Details for other side
24/7 Sydney Electrician
Marcus Pell
0431 587 219
marcus@brightwirehollow.com.au
brightwirehollow.com.au
icons for facebook, instagram, linked in

Industry/Entity Type

electrician

Contact Information for Business Card

company info

```html
<!DOCTYPE html>
<html lang="en">
<head>
<meta charset="utf-8">
<title>Brightwire Hollow — Business Cards</title>
<link href="https://fonts.googleapis.com/css2?family=Montserrat:wght@400;600;700&display=swap" rel="stylesheet">
<style>
  :root {
    --page-bg: #e7e4df;
    --card-dark: #0f0f0f;
    --card-light: #ffffff;
    --accent: #ee3a27;
    --text-light: #f2f2f2;
  }
  * { margin: 0; padding: 0; box-sizing: border-box; }
  html, body {
    width: 900px; height: 1200px; overflow: hidden;
    background: var(--page-bg);
    font-family: "Montserrat", sans-serif;
  }
  .card {
    position: absolute;
    left: 79px; width: 743px; height: 442px;
    border-radius: 22px;
    overflow: hidden;
    box-shadow: 0 6px 18px rgba(0,0,0,0.18);
  }
  .card--details { top: 130px; background: var(--card-dark); }
  .card--logo { top: 638px; height: 440px; background: var(--card-light); }

  .wordmark {
    position: absolute;
    color: var(--accent);
    font-weight: 700;
    text-transform: uppercase;
    line-height: 1.05;
  }
  .card--details .wordmark {
    left: 70px; top: 178px; width: 280px;
    font-size: 36px; letter-spacing: 1px;
  }
  .card--logo .wordmark {
    left: 0; right: 0; top: 152px;
    text-align: center;
    font-size: 62px; letter-spacing: 2px;
  }

  .divider {
    position: absolute; left: 361px; top: 102px;
    width: 2px; height: 204px; background: var(--accent);
  }
  .contacts { position: absolute; left: 376px; top: 100px; }
  .person { margin-bottom: 16px; }
  .person__name {
    color: var(--accent); font-weight: 600; font-size: 24px;
    margin-bottom: 6px;
  }
  .line {
    display: flex; align-items: center; gap: 10px;
    color: var(--text-light); font-size: 15px; font-weight: 400;
    letter-spacing: 0.3px;
  }
  .line svg { width: 15px; height: 15px; flex: none; fill: var(--accent); }
  .links { margin-top: 10px; }
  .links .line { margin-bottom: 15px; }

  .social {
    position: absolute; top: 346px; left: 333px;
    display: flex; gap: 10px;
  }
  .social__tile {
    width: 21px; height: 21px; border-radius: 4px; background: var(--accent);
  }

  .tagline {
    position: absolute; left: 0; right: 0; top: 398px; height: 25px;
    background: var(--accent);
    color: var(--text-light);
    font-size: 14px; font-weight: 400; letter-spacing: 0.5px;
    text-align: center; line-height: 25px;
  }
</style>
</head>
<body>

<section class="card card--details">
  <div class="wordmark">Brightwire<br>Hollow</div>
  <div class="divider"></div>

  <div class="contacts">
    <div class="person">
      <div class="person__name">Marcus Pell</div>
      <div class="line">
        <svg viewBox="0 0 24 24" aria-hidden="true"><path d="M6.6 10.8a15.1 15.1 0 0 0 6.6 6.6l2.2-2.2a1 1 0 0 1 1-.25 11.4 11.4 0 0 0 3.6.57 1 1 0 0 1 1 1V20a1 1 0 0 1-1 1A17 17 0 0 1 3 4a1 1 0 0 1 1-1h3.5a1 1 0 0 1 1 1c0 1.25.2 2.45.57 3.57a1 1 0 0 1-.25 1z"/></svg>
        0431 587 219
      </div>
    </div>
    <div class="person">
      <div class="person__name">Leon Varga</div>
      <div class="line">
        <svg viewBox="0 0 24 24" aria-hidden="true"><path d="M6.6 10.8a15.1 15.1 0 0 0 6.6 6.6l2.2-2.2a1 1 0 0 1 1-.25 11.4 11.4 0 0 0 3.6.57 1 1 0 0 1 1 1V20a1 1 0 0 1-1 1A17 17 0 0 1 3 4a1 1 0 0 1 1-1h3.5a1 1 0 0 1 1 1c0 1.25.2 2.45.57 3.57a1 1 0 0 1-.25 1z"/></svg>
        0452 318 764
      </div>
    </div>
    <div class="links">
      <div class="line">
        <svg viewBox="0 0 24 24" aria-hidden="true"><path d="M3 5h18a1 1 0 0 1 1 1v12a1 1 0 0 1-1 1H3a1 1 0 0 1-1-1V6a1 1 0 0 1 1-1zm9 7.2L20 7H4z"/></svg>
        service@brightwirehollow.com.au
      </div>
      <div class="line">
        <svg viewBox="0 0 24 24" aria-hidden="true"><path d="M12 2a10 10 0 1 0 0 20 10 10 0 0 0 0-20zm0 2c.9 0 2.2 1.9 2.8 5H9.2C9.8 5.9 11.1 4 12 4zM4.3 11h4.8c-.05.6-.1 1.3-.1 2s.05 1.4.1 2H4.7A8 8 0 0 1 4.3 11zm.9 6h4.2c.4 1.5 1 2.7 1.6 3.6A8 8 0 0 1 5.2 17zm4-8H5.2a8 8 0 0 1 5.8-4.6C10.3 5.3 9.7 7 9.2 9zM12 20c-.9 0-2.2-1.4-2.8-3h5.6c-.6 1.6-1.9 3-2.8 3zm3-5H9c-.1-.6-.1-1.3-.1-2s0-1.4.1-2h6c.1.6.1 1.3.1 2s0 1.4-.1 2zm-1.9-10.6A8 8 0 0 1 18.8 9h-4c-.4-2-1-3.7-1.7-4.6zM13 20.6c.6-.9 1.2-2.1 1.6-3.6h4.2a8 8 0 0 1-5.8 3.6zM14.9 15c.05-.6.1-1.3.1-2s-.05-1.4-.1-2h4.8a8 8 0 0 1-.4 4z"/></svg>
        www.brightwirehollow.com.au
      </div>
    </div>
  </div>

  <div class="social" aria-label="Social media">
    <span class="social__tile"></span>
    <span class="social__tile"></span>
  </div>

  <div class="tagline">24/7 SYDNEY ELECTRICIANS</div>
</section>

<section class="card card--logo">
  <div class="wordmark">Brightwire<br>Hollow</div>
</section>

</body>
</html>
```